Buisness Card for an Agricultural Contracting and Earthmoving Company

We need a business card for a new business based in Ashbridge, Victoria. We are a company that specialises in two areas the first is and Earthmoving company, we do large jobs such as soccer fields to small jobs such as house cuts and riding arena's, drainage, and dams. The other side of the business specialises in Agricultural improvements and hay contracting. We require a card to represent both sides of the business. Must have the following information: Dale Morcombe, 2741 Bracken Rd, Ashbridge Victoria 3795, ph:03 5902 4638, mob: 0427 913 684, e-mail: dale@morcombeworks.com.au. Earthmoving and Agricultural Contracting.

Target Market(s)

Builder's, Council's, new home buyers, Farmers

Industry/Entity Type

House

Font styles to use
Sans Serif

Colors
ec2026
000000
5c5c5c
ffffff

Requirements
Must have
• Both facets of the business represented. Company logo

```html
<!DOCTYPE html>
<html lang="en">
<head>
<meta charset="utf-8">
<title>Morcombe Works – Business Card</title>
<link href="https://fonts.googleapis.com/css2?family=Roboto:wght@300;400;700&display=swap" rel="stylesheet">
<style>
  :root {
    --brand-red: #ec2026;
    --ink: #000000;
    --charcoal: #2b2424;
    --slate: #5c5c5c;
    --paper: #ffffff;
    --card-white: #ececec;
    --backdrop: #d9d6d2;
  }
  * { margin: 0; padding: 0; box-sizing: border-box; }
  html, body {
    width: 1200px; height: 900px; overflow: hidden;
    background: var(--backdrop);
    font-family: "Roboto", Arial, sans-serif;
  }
  .canvas {
    position: relative; width: 1200px; height: 900px;
    display: flex; flex-direction: column; align-items: center; justify-content: center; gap: 48px;
  }
  .card {
    position: relative; width: 560px; height: 320px;
    border-radius: 4px;
    box-shadow: 0 10px 26px rgba(0,0,0,.22);
    overflow: hidden;
  }

  /* Front */
  .card-front {
    background: radial-gradient(ellipse at 50% 40%, #d3232b 0%, #8c1219 38%, var(--charcoal) 85%);
    color: var(--paper);
    display: flex; flex-direction: column; align-items: center; justify-content: center;
  }
  .front-brand { display: flex; align-items: center; gap: 14px; }
  .brand-square { width: 30px; height: 30px; background: var(--paper); flex: none; }
  .front-brand .brand-name {
    font-weight: 700; font-size: 34px; letter-spacing: 1px;
    text-transform: uppercase; color: var(--paper);
  }
  .front-tagline {
    margin-top: 22px; font-size: 17px; font-weight: 400; letter-spacing: .3px;
    color: var(--paper);
  }

  /* Back */
  .card-back { background: var(--card-white); display: flex; }
  .back-brand {
    width: 50%;
    display: flex; flex-direction: column; align-items: center; justify-content: center; gap: 12px;
    padding-top: 60px;
  }
  .back-brand .brand-square { width: 44px; height: 44px; background: var(--brand-red); }
  .back-brand .brand-name {
    font-weight: 700; font-size: 22px; letter-spacing: .8px;
    text-transform: uppercase; color: var(--brand-red); white-space: nowrap;
  }
  .contact { width: 50%; padding: 58px 0 0 24px; color: var(--slate); }
  .contact-name {
    font-weight: 300; font-size: 22px; text-transform: uppercase; color: var(--charcoal);
    letter-spacing: .5px;
  }
  .contact-role { font-size: 12px; margin-top: 2px; font-weight: 400; }
  .contact-rule { height: 1.5px; background: var(--brand-red); margin: 12px 0 14px 0; }
  .contact-lines { list-style: none; font-size: 12.5px; line-height: 1.45; font-weight: 300; color: var(--charcoal); }
  .contact-lines .label { color: var(--brand-red); font-weight: 400; display: inline-block; width: 16px; }
  .contact-address { margin-top: 16px; font-size: 12.5px; line-height: 1.45; font-weight: 300; color: var(--charcoal); }
</style>
</head>
<body>
<main class="canvas">
  <section class="card card-front" aria-label="Card front">
    <div class="front-brand">
      <span class="brand-square"></span>
      <span class="brand-name">Morcombe Works</span>
    </div>
    <p class="front-tagline">Earthmoving and Agricultural Contracting</p>
  </section>

  <section class="card card-back" aria-label="Card back">
    <div class="back-brand">
      <span class="brand-square"></span>
      <span class="brand-name">Morcombe Works</span>
    </div>
    <div class="contact">
      <h1 class="contact-name">Dale Morcombe</h1>
      <p class="contact-role">Director</p>
      <div class="contact-rule"></div>
      <ul class="contact-lines">
        <li><span class="label">T</span>03 5902 4638</li>
        <li><span class="label">M</span>0427 913 684</li>
        <li><span class="label">E</span>dale@morcombeworks.com.au</li>
      </ul>
      <p class="contact-address">2741 Bracken Rd,<br>Ashbridge Victoria 3795</p>
    </div>
  </section>
</main>
</body>
</html>
```